Uprising SaaS company needs an attractive business card design

We're an uprising SaaS company who's attempting to attack the rigid car (insurance) claims management market in Europe.
We want to our mighty base order management system, listen to our clients to connect the smart ideas to build something even mightier.
We primarily focus on helping our customers manage their customers' claims/orders and get them resolved as smoothly as possible.
We'd like the business card design to express technical innovation and the fact that we connect smart ideas, as our company slogan indicates.
Contact Information for Business Card
Name, position, website, email, mobile, business address
Font styles to use
Colors
Designer to choose colors to be used in the design.
Look and feel
Each slider illustrates characteristics of the customer's brand and the style your logo design should communicate.

```html
<!DOCTYPE html>
<html lang="en">
<head>
<meta charset="utf-8">
<title>Nexoral business card</title>
<link rel="stylesheet" href="https://fonts.googleapis.com/css2?family=Arimo:wght@400;700&display=swap">
<style>
  :root {
    --backdrop: #2c2c2e;
    --brand-blue: #84cfe3;
    --accent-blue: #6cc4df;
    --line-blue: #7fbfd2;
    --card-white: #ffffff;
    --ink-grey: #7a7a7a;
    --ink-dark: #4a4a4a;
  }
  * { box-sizing: border-box; margin: 0; padding: 0; }
  html, body {
    width: 1200px; height: 960px; overflow: hidden;
    background: var(--backdrop);
    font-family: "Arimo", Arial, sans-serif;
  }
  .stage { position: relative; width: 1200px; height: 960px; }
  .card {
    position: absolute; width: 700px; height: 400px;
    border-radius: 28px;
    box-shadow: 0 18px 40px rgba(0,0,0,.45);
  }
  .card-front { left: 80px; top: 60px; background: var(--brand-blue); }
  .card-back { left: 420px; top: 500px; background: var(--card-white); }

  .wordmark {
    display: flex; align-items: center; gap: 10px;
    font-weight: 400; letter-spacing: 1px;
  }
  .wordmark-dot { width: 12px; height: 12px; border-radius: 50%; }
  .card-front .wordmark {
    position: absolute; left: 50%; top: 50%; transform: translate(-50%, -50%);
    font-size: 96px; color: var(--card-white);
  }
  .card-front .wordmark-dot { width: 16px; height: 16px; background: var(--card-white); }
  .card-back .wordmark {
    position: absolute; right: 50px; top: 48px;
    font-size: 58px; color: var(--ink-grey);
  }
  .card-back .wordmark-dot { background: var(--accent-blue); }

  .divider {
    position: absolute; left: 50px; right: 50px; top: 250px;
    border-top: 2px dashed var(--line-blue);
  }
  .identity { position: absolute; left: 50px; top: 192px; }
  .person-name { font-weight: 700; font-size: 26px; color: var(--ink-grey); letter-spacing: .5px; }
  .person-role { font-size: 18px; color: var(--accent-blue); margin-top: 2px; }

  .address {
    position: absolute; right: 50px; top: 160px;
    text-align: right; font-size: 16px; line-height: 1.35; color: var(--ink-dark);
  }
  .contacts {
    position: absolute; left: 90px; top: 278px;
    list-style: none; font-size: 18px; color: var(--ink-dark); line-height: 1.55;
  }
  .contacts li { display: flex; align-items: center; gap: 12px; }
  .contact-icon { width: 16px; height: 16px; flex: none; }
</style>
</head>
<body>
<main class="stage">
  <section class="card card-front">
    <div class="wordmark"><span class="wordmark-dot"></span>nexoral</div>
  </section>

  <section class="card card-back">
    <div class="wordmark"><span class="wordmark-dot"></span>nexoral</div>

    <address class="address">
      Nexoral Group<br>
      214 Linden Court<br>
      Fairview, Oregon 97024
    </address>

    <div class="identity">
      <p class="person-name">DANIEL BROOKS</p>
      <p class="person-role">President</p>
    </div>

    <div class="divider"></div>

    <ul class="contacts">
      <li>
        <svg class="contact-icon" viewBox="0 0 16 16"><rect x="4" y="1" width="8" height="14" rx="1.5" fill="none" stroke="#6cc4df" stroke-width="1.6"/><circle cx="8" cy="12.5" r=".9" fill="#6cc4df"/></svg>
        555-014-2290
      </li>
      <li>
        <svg class="contact-icon" viewBox="0 0 16 16"><rect x="1" y="3" width="14" height="10" rx="1" fill="#6cc4df"/><path d="M1.5 3.5 8 9l6.5-5.5" fill="none" stroke="#fff" stroke-width="1.3"/></svg>
        info@nexoral.com
      </li>
      <li>
        <svg class="contact-icon" viewBox="0 0 16 16"><circle cx="8" cy="8" r="7" fill="#6cc4df"/><path d="M1 8h14M8 1c-3 3.5-3 10.5 0 14M8 1c3 3.5 3 10.5 0 14" fill="none" stroke="#fff" stroke-width="1"/></svg>
        nexoral.com
      </li>
    </ul>
  </section>
</main>
</body>
</html>
```